**Kestrel Joinery Works Limited**

We need a website for a renovation/remodeling company based in Hamilton, New Zealand. Ideally it will catch clients' attention and be modern and professional looking. I have attached a logo that I have just recently had made (through PixelForge). If the website could reflect this style and colour schemes, that would be awesome. The final design should communicate a trustworthiness and professionalism.

I have attached photos of a website that I really think is great, so if we could have something that follows along those likes,

https://www.dailyquillpost.example/local-news/news/hamilton-builder-named-top-apprentice-in-region/QXPLTZ8VRA3MJ5FDYHUNCESKWB/

I won a competition a few years ago while I was an apprentice, If we could somehow put that in there as one of my achievements to try to bring in some trust that would be awesome. I would like to add a new picture though because my beard in that photo is wild.

Target Market(s)

Families that want live in the homes that i'm working on. not investors. People that are looking for quality not cheapest price.

Industry/Entity Type

Construction, Home renovations, Maintenance, Deck Builds, New Builds, Bathrooms, Kitchens

Coding

Number of Pages Required

5+ page

Font styles to use
Sans Serif

Colors
6B429C
8869AF
B7A5CE
E3DAEB
F3F0F8

Requirements
Must have
• Contact us page, large clear pictures, Colours the work with the purple in my logo. That will be my company colour so I'm thinking black and purple, or what ever compliments purple nicely
Nice to have
• Page for Renovations, Testimonials, Contact us, Home, About us
Should not have
• Plain looking pages, empty white space, I want the text to be beside a nice big picture etc

```html
<!DOCTYPE html>
<html lang="en">
<head>
<meta charset="utf-8">
<title>Kestrel Joinery Works Limited</title>
<link href="https://fonts.googleapis.com/css2?family=Red+Hat+Display:wght@400;500;600;700&display=swap" rel="stylesheet">
<style>
:root{
  --purple:#6a2d91;
  --purple-dark:#4f1f6e;
  --purple-light:#8869af;
  --lilac:#b7a5ce;
  --dark:#2b2b2b;
  --black:#151515;
  --white:#ffffff;
  --text:#333333;
}
*{margin:0;padding:0;box-sizing:border-box}
html,body{width:1200px;height:4594px;overflow:hidden}
body{position:relative;font-family:"Red Hat Display",Arial,sans-serif;color:var(--text);background:var(--white)}
.abs{position:absolute}
.btn{position:absolute;display:flex;align-items:center;justify-content:center;font-weight:700;font-size:16px;color:var(--white);background:var(--purple);clip-path:polygon(0 0,100% 0,calc(100% - 18px) 100%,0 100%);text-decoration:none}
.btn::after{content:"";position:absolute;right:0;top:0;width:22px;height:100%;background:var(--purple-light);clip-path:polygon(80% 0,100% 0,20% 100%,0 100%)}
.btn.black{background:var(--black)}
.btn.white{background:var(--white);color:var(--black)}
.btn.white::after{background:var(--lilac)}
.photo{position:absolute}

/* header */
.logo{position:absolute;left:107px;top:22px;width:110px;color:var(--white);font-weight:700;font-size:14px;line-height:1.1;text-align:center;display:flex;flex-direction:column;align-items:center;gap:6px}
.logo .mark{width:14px;height:14px;background:var(--white);border-radius:50%}
.nav{position:absolute;top:38px;left:0;font-size:16px;color:var(--white)}
.nav a{position:absolute;color:var(--white);text-decoration:none;white-space:nowrap}
.nav a.active::after{content:"";position:absolute;left:0;right:0;bottom:-6px;height:2px;background:var(--white)}
.hero-title{position:absolute;left:105px;top:218px;font-size:58px;line-height:76px;font-weight:700;color:var(--white);text-shadow:0 2px 8px rgba(0,0,0,.25)}
.dots{position:absolute;display:flex;gap:9px}
.dots span{width:11px;height:11px;border-radius:50%;border:1.5px solid var(--white)}
.dots span.on{background:var(--white)}

/* about */
.eyebrow{font-size:18px;font-weight:600;color:var(--purple);text-transform:uppercase}
.h2{font-weight:700;color:var(--black)}
.badge{position:absolute;left:546px;top:888px;width:132px;height:132px;border-radius:50%;background:var(--dark);border:4px solid var(--white);color:var(--white);text-align:center;display:flex;flex-direction:column;justify-content:center;font-size:13px}
.badge b{font-size:50px;line-height:46px;font-weight:500}

/* renovations */
.services{position:absolute;left:554px;top:1396px;width:540px;height:357px;display:grid;grid-template-columns:repeat(3,1fr);grid-template-rows:repeat(2,1fr)}
.service{display:flex;flex-direction:column;align-items:center;justify-content:center;text-align:center;font-size:16px;font-weight:600;line-height:21px;gap:14px}
.service.light{background:var(--white);color:var(--purple)}
.service.darkc{background:var(--black);color:var(--white)}
.service svg{width:48px;height:48px;fill:none;stroke:currentColor;stroke-width:2;stroke-linejoin:round}

/* projects */
.card{position:absolute;top:2109px;width:232px;height:262px;background:var(--black)}
.card .pic{height:211px}
.card .label{height:51px;display:flex;align-items:center;justify-content:center;color:var(--white);font-weight:700;font-size:16px;background:#1b1b1b}
.card.active .label{background:var(--purple)}

/* footer */
.f-head{position:absolute;top:4216px;font-size:17px;font-weight:700;color:var(--white);text-transform:uppercase}
.f-list{position:absolute;list-style:none;color:var(--white);font-size:14px}
.f-list li{height:32.5px}
.field{position:absolute;background:var(--purple-dark);color:var(--white);font-size:13px;padding:10px 12px}
.social{position:absolute;top:4406px;width:24px;height:24px;border-radius:50%;background:var(--purple-dark);border:1.5px solid var(--lilac)}
.contact-line{position:absolute;left:718px;display:flex;align-items:center;gap:20px;font-size:15px;color:var(--text);line-height:22px}
.contact-line i{width:38px;height:38px;border-radius:50%;background:var(--purple);display:flex;align-items:center;justify-content:center;flex:none}
</style>
</head>
<body>

<!-- HERO -->
<svg class="abs" style="left:0;top:0" width="1200" height="660" viewBox="0 0 1200 660">
  <defs>
    <linearGradient id="heroBase" x1="0" y1="0" x2="1" y2="0">
      <stop offset="0" stop-color="#4b2a72"/>
      <stop offset="0.35" stop-color="#5f3a8a"/>
      <stop offset="0.62" stop-color="#6b4c86"/>
      <stop offset="0.8" stop-color="#8a5a34"/>
      <stop offset="1" stop-color="#b7c7d4"/>
    </linearGradient>
    <radialGradient id="heroFloor" cx="0.35" cy="1" r="0.55">
      <stop offset="0" stop-color="#7c8a80" stop-opacity=".85"/>
      <stop offset="1" stop-color="#7c8a80" stop-opacity="0"/>
    </radialGradient>
    <radialGradient id="heroWood" cx="0.74" cy="0.55" r="0.22">
      <stop offset="0" stop-color="#e2b872" stop-opacity=".9"/>
      <stop offset="1" stop-color="#e2b872" stop-opacity="0"/>
    </radialGradient>
    <radialGradient id="heroChair" cx="0.44" cy="0.55" r="0.18">
      <stop offset="0" stop-color="#3a3a3e" stop-opacity=".8"/>
      <stop offset="1" stop-color="#3a3a3e" stop-opacity="0"/>
    </radialGradient>
  </defs>
  <g role="img" aria-label="Photo of a living room with purple wall panels, grey armchair, lamp, wooden cabinet and a window">
    <polygon points="0,0 1200,0 1200,512 310,632 0,506" fill="url(#heroBase)"/>
    <polygon points="0,0 1200,0 1200,512 310,632 0,506" fill="url(#heroFloor)"/>
    <polygon points="0,0 1200,0 1200,512 310,632 0,506" fill="url(#heroChair)"/>
    <polygon points="0,0 1200,0 1200,512 310,632 0,506" fill="url(#heroWood)"/>
  </g>
  <polygon points="300,633 1200,512 1200,530 320,648" fill="var(--purple)"/>
</svg>
<div class="logo"><span class="mark"></span>KESTREL JOINERY WORKS LTD</div>
<nav class="nav">
  <a class="active" style="left:289px">Home</a>
  <a style="left:367px">About</a>
  <a style="left:448px">Renovations</a>
  <a style="left:578px">Projects</a>
  <a style="left:676px">Testimonial</a>
  <a style="left:795px">Contact</a>
</nav>
<a class="btn" style="left:897px;top:30px;width:192px;height:38px;font-size:15px">
  <svg width="16" height="16" viewBox="0 0 24 24" style="margin-right:10px"><path fill="#fff" d="M6.6 10.8a15 15 0 0 0 6.6 6.6l2.2-2.2c.3-.3.7-.4 1-.2 1.1.4 2.3.6 3.6.6.6 0 1 .4 1 1V20c0 .6-.4 1-1 1A17 17 0 0 1 3 4c0-.6.4-1 1-1h3.5c.6 0 1 .4 1 1 0 1.3.2 2.5.6 3.6.1.3 0 .7-.2 1z"/></svg>
  +64 27 555 0193
</a>
<h1 class="hero-title">Your Trusted Partner<br>For Home Renovations</h1>
<a class="btn" style="left:107px;top:396px;width:148px;height:37px">Contact Us</a>
<div class="dots" style="left:106px;top:482px"><span class="on"></span><span></span><span></span></div>

<!-- ABOUT -->
<div class="photo" style="left:0;top:745px;width:613px;height:416px;background:radial-gradient(ellipse 30% 40% at 72% 62%,rgba(140,150,90,.9),rgba(140,150,90,0)),radial-gradient(ellipse 25% 35% at 62% 42%,rgba(240,240,238,.85),rgba(240,240,238,0)),linear-gradient(90deg,#9a9a92 0%,#c9c6b8 25%,#b9ad72 45%,#d8d2bd 70%,#c6b892 100%)" role="img" aria-label="Builder installing insulation batts between timber wall framing"></div>
<div class="abs" style="left:613px;top:745px;width:20px;height:416px;background:linear-gradient(90deg,#b07b3c,#8e5e28)"></div>
<div class="badge"><span>Experienced</span><b>10</b><span>YEARS</span></div>
<div class="abs eyebrow" style="left:697px;top:782px">Welcome To</div>
<h2 class="abs h2" style="left:697px;top:810px;font-size:32px;line-height:42px;font-weight:600">Kestrel Joinery Works<br>Limited</h2>
<p class="abs" style="left:697px;top:912px;width:390px;font-size:15px;line-height:24px">Your trusted partner for home renovations, general building work, maintenance, decks, and interior and exterior projects. With over a decade of experience in the trade, we are a qualified builder and hold an LBP license.</p>
<a class="btn" style="left:699px;top:1057px;width:152px;height:41px">About Us</a>

<!-- RENOVATIONS -->
<svg class="abs" style="left:0;top:1225px" width="1200" height="70"><polygon points="360,66 1040,5 1200,66" fill="var(--black)"/></svg>
<section class="abs" style="left:0;top:1291px;width:1200px;height:585px;background:var(--purple)"></section>
<h2 class="abs" style="left:107px;top:1420px;font-size:38px;font-weight:600;color:var(--white)">Renovations</h2>
<p class="abs" style="left:107px;top:1490px;width:400px;font-size:15px;line-height:25.7px;color:var(--white)">We take pride in serving the Hamilton area with our expertise and commitment to quality craftsmanship. Whether you're looking to renovate your home, need general building work, or have maintenance and repair needs, Kestrel Joinery Works Limited is here to bring your vision to life. Expect excellence, reliability, and professionalism in every project we undertake.</p>
<a class="btn black" style="left:107px;top:1703px;width:152px;height:40px">View All</a>
<div class="services">
  <div class="service light"><svg viewBox="0 0 48 48"><path d="M10 8h16l6 24H16z"/><path d="M28 30l10-6 4 6-10 8z"/></svg>Plaster<br>Boarding</div>
  <div class="service darkc"><svg viewBox="0 0 48 48"><rect x="6" y="26" width="30" height="16"/><path d="M6 34h30M16 26v8M26 34v8M30 26l12-16M38 8l6 4"/></svg>Cladding<br>Services</div>
  <div class="service light"><svg viewBox="0 0 48 48"><rect x="4" y="10" width="40" height="28"/><path d="M4 30l20-20M12 38l28-28M24 38l20-20M36 38l8-8"/></svg>Flooring<br>Renovations</div>
  <div class="service darkc"><svg viewBox="0 0 48 48"><path d="M8 44V16a16 16 0 0 1 32 0v28M8 44h32M16 44V14M24 44V8M32 44V14M8 24h32"/></svg>Fencing &amp;<br>Gates</div>
  <div class="service light"><svg viewBox="0 0 48 48"><rect x="6" y="22" width="36" height="20"/><path d="M24 22v20M18 22v-8h12v8M24 14V6M20 8h8M14 32h4M30 32h4"/></svg>Bathrooms<br>Renovations</div>
  <div class="service darkc"><svg viewBox="0 0 48 48"><path d="M8 40l24-24M14 6l10 10-4 4L10 10zM40 40L16 16M34 6l8 8-6 6-8-8z"/></svg>Carpentry<br>Services</div>
</div>

<!-- PROJECTS -->
<section class="abs" style="left:0;top:1876px;width:1200px;height:670px;background:var(--dark)"></section>
<svg class="abs" style="left:0;top:1876px" width="1200" height="90"><polygon points="30,0 1200,0 1200,12 170,80" fill="var(--black)"/></svg>
<div class="abs" style="left:0;top:1984px;width:1200px;text-align:center;color:var(--white);font-size:18px;font-weight:500">PROJECTS</div>
<h2 class="abs" style="left:0;top:2012px;width:1200px;text-align:center;color:var(--white);font-size:38px;font-weight:600">Excellence, Reliability, And Professionalism</h2>
<div class="card" style="left:103px"><div class="pic" style="background:radial-gradient(ellipse 50% 20% at 50% 82%,rgba(60,110,100,.8),rgba(60,110,100,0)),linear-gradient(180deg,#8b6a52 0%,#6d4f3b 45%,#4c382b 75%,#a08a76 100%)" role="img" aria-label="Living room with timber panelled walls and green sofa"></div><div class="label">Lorem Ipsum Dollar</div></div>
<div class="card active" style="left:356px"><div class="pic" style="background:radial-gradient(ellipse 50% 18% at 45% 78%,rgba(70,110,90,.7),rgba(70,110,90,0)),linear-gradient(180deg,#b07a4a 0%,#e6ddd0 35%,#f1ece4 65%,#9f8a70 100%)" role="img" aria-label="Bright lounge with exposed timber ceiling beams"></div><div class="label">Lorem Ipsum Dollar</div></div>
<div class="card" style="left:608px"><div class="pic" style="background:linear-gradient(90deg,#d9dadb 0%,#f3f3f1 30%,#6f7378 45%,#9a9ea3 55%,#eeeeec 75%,#d4d6d8 100%)" role="img" aria-label="White kitchen with steel fridge"></div><div class="label">Lorem Ipsum Dollar</div></div>
<div class="card" style="left:861px"><div class="pic" style="background:radial-gradient(ellipse 30% 20% at 40% 80%,rgba(214,180,120,.8),rgba(214,180,120,0)),linear-gradient(180deg,#f4f3f0 0%,#eceae5 55%,#d2c7b4 100%)" role="img" aria-label="Kitchen cabinetry being installed"></div><div class="label">Lorem Ipsum Dollar</div></div>
<a class="btn" style="left:524px;top:2414px;width:152px;height:41px">View All</a>

<!-- TESTIMONIAL -->
<section class="abs" style="left:0;top:2546px;width:469px;height:592px;background:var(--purple)"></section>
<div class="photo" style="left:469px;top:2546px;width:731px;height:592px;background:radial-gradient(ellipse 40% 18% at 55% 68%,rgba(196,140,80,.95),rgba(196,140,80,0)),radial-gradient(ellipse 35% 25% at 60% 88%,rgba(200,200,204,.8),rgba(200,200,204,0)),linear-gradient(180deg,#d9d8d5 0%,#efefed 25%,#5e5c58 45%,#6e6b66 60%,#3f3d3b 80%,#8f8c88 100%)" role="img" aria-label="Modern kitchen with grey cabinets, white tiles and wooden dining table"></div>
<h2 class="abs" style="left:98px;top:2578px;font-size:38px;font-weight:600;color:var(--white)">Testimonial</h2>
<div class="abs" style="left:106px;top:2713px;width:46px;height:46px;border-radius:50%;background:var(--white);color:var(--purple);font-size:30px;font-weight:700;text-align:center;line-height:52px">&ldquo;</div>
<p class="abs" style="left:109px;top:2780px;width:335px;font-size:15px;line-height:25.7px;color:var(--white)">“We had an internal door (invisible door) installed across the hallway to effectively break the house into two living areas - plus internal door to secure internal garage. Kestrel Joinery (Callum) completed the job to a high standard and left the house clean and tidy. I'd recommend him to anyone. Very professional and immaculate craftsmanship.”</p>
<p class="abs" style="left:109px;top:3022px;font-size:15px;line-height:23px;color:var(--white)">- Maree T<br>Client</p>
<div class="dots" style="left:107px;top:3087px;gap:5px"><span class="on" style="width:6px;height:6px;border-width:1px"></span><span style="width:6px;height:6px;border-width:1px"></span><span style="width:6px;height:6px;border-width:1px"></span><span style="width:6px;height:6px;border-width:1px"></span></div>

<!-- CALL TO ACTION -->
<div class="photo" style="left:0;top:3138px;width:1200px;height:424px;background:radial-gradient(ellipse 12% 10% at 18% 10%,rgba(210,160,90,.55),rgba(210,160,90,0)),radial-gradient(ellipse 12% 10% at 82% 10%,rgba(210,160,90,.55),rgba(210,160,90,0)),radial-gradient(ellipse 35% 25% at 50% 80%,rgba(120,110,100,.6),rgba(120,110,100,0)),linear-gradient(180deg,#3b3631 0%,#2e2a26 40%,#3a342d 70%,#1f1b18 100%)" role="img" aria-label="Dimly lit bathroom with vanity, mirrors and wall lights"></div>
<div class="abs" style="left:0;top:3273px;width:1200px;text-align:center;color:var(--white);font-size:18px;font-weight:500">LOCATED IN FERNVALE</div>
<h2 class="abs" style="left:0;top:3303px;width:1200px;text-align:center;color:var(--white);font-size:38px;font-weight:600">Coming Home To Excellence Today</h2>
<a class="btn" style="left:524px;top:3368px;width:152px;height:40px">Contact Us</a>

<!-- CONTACT -->
<svg class="abs" style="left:100px;top:3630px" width="560" height="410">
  <defs>
    <linearGradient id="portraitGrad" x1="0" y1="0" x2="0" y2="1">
      <stop offset="0" stop-color="#d8d4cf"/>
      <stop offset="0.5" stop-color="#8d7766"/>
      <stop offset="1" stop-color="#3e4146"/>
    </linearGradient>
    <linearGradient id="frameGrad" x1="0" y1="0" x2="1" y2="1">
      <stop offset="0" stop-color="#c99a5e"/>
      <stop offset="0.45" stop-color="#e8dccb"/>
      <stop offset="0.6" stop-color="#3f4a5a"/>
      <stop offset="0.8" stop-color="#d6b07a"/>
      <stop offset="1" stop-color="#f0ebe3"/>
    </linearGradient>
  </defs>
  <polygon points="10,165 203,165 107,7" fill="url(#portraitGrad)" role="img" aria-label="Portrait of the builder"/>
  <polygon points="319,16 87,403 547,403" fill="url(#frameGrad)" role="img" aria-label="Builder fitting ceiling framing in a new build"/>
</svg>
<h2 class="abs h2" style="left:699px;top:3664px;font-size:36px;font-weight:600">Get In Touch</h2>
<div class="contact-line" style="top:3749px"><i><svg width="16" height="18" viewBox="0 0 24 24"><path fill="#fff" d="M12 2a7 7 0 0 0-7 7c0 5 7 13 7 13s7-8 7-13a7 7 0 0 0-7-7zm0 9.5A2.5 2.5 0 1 1 12 6.5a2.5 2.5 0 0 1 0 5z"/></svg></i><span>14 Larchmont Place Fernvale Hamilton<br>3210 New Zealand</span></div>
<div class="contact-line" style="top:3818px"><i><svg width="16" height="16" viewBox="0 0 24 24"><path fill="#fff" d="M6.6 10.8a15 15 0 0 0 6.6 6.6l2.2-2.2c.3-.3.7-.4 1-.2 1.1.4 2.3.6 3.6.6.6 0 1 .4 1 1V20c0 .6-.4 1-1 1A17 17 0 0 1 3 4c0-.6.4-1 1-1h3.5c.6 0 1 .4 1 1 0 1.3.2 2.5.6 3.6.1.3 0 .7-.2 1z"/></svg></i><span>027 555 0193</span></div>
<div class="contact-line" style="top:3880px"><i><svg width="16" height="14" viewBox="0 0 24 20"><rect x="1" y="1" width="22" height="18" rx="2" fill="#fff"/><path d="M2 3l10 8 10-8" stroke="#6a2d91" stroke-width="2" fill="none"/></svg></i><span>hello@kestreljoinery.example</span></div>
<a class="btn" style="left:699px;top:3962px;width:192px;height:41px">Get Directions</a>

<!-- FOOTER -->
<svg class="abs" style="left:0;top:4070px" width="1200" height="150">
  <polygon points="0,147 880,12 880,22 0,150" fill="var(--black)"/>
  <polygon points="0,150 1035,2 1200,150" fill="var(--purple)"/>
</svg>
<footer class="abs" style="left:0;top:4218px;width:1200px;height:376px;background:var(--purple)"></footer>
<div class="abs" style="left:105px;top:4268px;width:172px;color:var(--white);font-weight:700;font-size:18px;line-height:1.15;text-align:center;display:flex;flex-direction:column;align-items:center;gap:8px"><span style="width:16px;height:16px;border-radius:50%;background:var(--white)"></span>KESTREL JOINERY WORKS LTD</div>
<span class="social" style="left:109px"></span><span class="social" style="left:150px"></span><span class="social" style="left:189px"></span><span class="social" style="left:230px"></span>

<div class="f-head" style="left:337px">Quick Link</div>
<ul class="f-list" style="left:340px;top:4258px">
  <li>›&nbsp;&nbsp;&nbsp;&nbsp;Home</li><li>›&nbsp;&nbsp;&nbsp;&nbsp;About</li><li>›&nbsp;&nbsp;&nbsp;&nbsp;Renovations</li><li>›&nbsp;&nbsp;&nbsp;&nbsp;Projects</li><li>›&nbsp;&nbsp;&nbsp;&nbsp;Testimonial</li><li>›&nbsp;&nbsp;&nbsp;&nbsp;Contact</li>
</ul>
<div class="f-head" style="left:515px">Opening Hour</div>
<ul class="f-list" style="left:517px;top:4258px">
  <li>Mon: Fri</li><li>7:00am – 5:00pm</li><li>Sat: Closed</li><li>Sun : Closed</li>
</ul>
<div class="f-head" style="left:720px">Contact Us</div>
<div class="field" style="left:720px;top:4267px;width:181px;height:35px">First Name</div>
<div class="field" style="left:904px;top:4267px;width:189px;height:35px">Last Name</div>
<div class="field" style="left:720px;top:4308px;width:181px;height:36px">Email</div>
<div class="field" style="left:904px;top:4308px;width:189px;height:36px">Phone</div>
<div class="field" style="left:720px;top:4351px;width:373px;height:84px">Message</div>
<a class="btn white" style="left:720px;top:4443px;width:152px;height:41px">Submit Now</a>

<div class="abs" style="left:0;top:4543px;width:1200px;height:51px;background:var(--purple-dark);color:var(--white);font-size:11px;display:flex;align-items:center;justify-content:center">© 2023 KESTRELJOINERYWORKSLTD All right reserved</div>

</body>
</html>
```